Hurricane Damage Public Adjuster Billboard

I have created several projects with you and have several great designs. I need to format them into a Billboard for upcoming Hurricane Season. Need done in a month. Im also in process of getting an eye catching and easy to remember 800# Vanity phone number like Call 800-Stormsafe or 800- Need Help? My included past Pixel Bazaar projects will give you an idea of what colors, schemes, and designs I gravitate towards. 3 past Design projects were 1) 2 Logos where I picked the 1st place and the 2nd place and 2) Index Card where I picked the winner as the Index Card and the 2nd place as a Post Card. Point is, I will pick and pay for 2 winners if they're good. This should help to sweeten the pot. Also, please look at my website for ideas that I like:

www.CedarlineClaimHelp.com
I want people to feel that I am the best and highest. Level.

I've been getting a lot of quick half effort designs basically cut & pasting my previous projects. Please don't rush and take your time to be creative. A an example, my Biggest Competitor is Tamarack Public Adjusting. Their colors are Black and Gold while mine are Blue, White, and Black with a highlight of Orange if possible. I JUST imported a picture of their BillBoard. I need mine better and BLOW AWAY THEIRS. Terms like "Don't be Victimized Twice ?, Don't let the Hurricane Ruin your Life?". "Get Fairly Paid & Move On" "Our Clients Claims are VIP?
Updates

I'm getting a lot of quick half effort ones. I'd rather you take your time and really put some thoughts and effort into it. My Biggest Competitor is Tamarack Public Adjusting. They have black & gold colors, while I have Blue, Black, and white.

It needs to blow theirs away. I have imported their Billboard for comparative purposes.

Guy's,
I'll make it easier for you in what I'm looking for. Please look at the Tamarack Billboard picture attached.

1) Put my "Blue Shield" to the left, replacing their logo
2) change color patterns from their (Black, Gold, White) to my color schemes of (Black, Blue, White)
3) I want to see my name where their is:

THE
Cedarline Claim Help
EXPERT & LOCAL Public Adjusters
"FOR THE POLICYHOLDER!!"

4) to the right, add the A+Rated logo and QRT+ Accredited logo, 5 Star Zorvex Rated logo, 5 Start PORCHLINK Highly Rated logo, etc..

5) the right side is where you can be creative as I will not have a picture of me there.

"20+ Years of Experience, Recovering Millions for our VIP Clients"

"Your Best, Locally-Based Private Adjuster & Advocate'
"FOR THE POLICYHOLDER!!"

"Don't be victimized Twice!!"

"Don't let the Hurricane Ruin Your Life!!"

This should really help. Also, refer to my website, maybe a couple testimonial fillers?

Thanks all,

marcus@CedarlineClaimHelp.com

Just imported a few awards that would look great to the right side with all the other 5 Star Ratings and accolades.
This right section could be titled like zmy Website:

5 Star Reviews, Ratings & Awards:
4-5 Logos underneath?

Target Market(s)

Coastal place where a Hurricane 🌀 🌀 Hits

Industry/Entity Type

Hurricane Public Insurance Adjuster

Font styles to use
Sans Serif
Other font styles liked:
• Zurich fonts

Colors
0054AA
0677BA
7BADD7
CADEEF
E8F1F8
EE7325
F08F49
F5BC92
FAE3D3
FDF4ED

Requirements
Must have
• Use my past project logos, colors, and schemes to create eye grabbing BillBoard
Nice to have
Should not have
• Not be too busy, must be Easy to Read, Eye Catchy

```html
<!DOCTYPE html>
<html lang="en">
<head>
<meta charset="utf-8">
<title>Cedarline Claim Help – Hurricane Billboard</title>
<link href="https://fonts.googleapis.com/css2?family=Cinzel:wght@500;600;700&family=Montserrat:wght@500;600;700&family=Open+Sans:ital,wght@1,700&display=swap" rel="stylesheet">
<style>
  :root{
    --page:#d0d0d0;
    --sky:#1596d4;
    --navy:#1a3d8c;
    --deep:#142f78;
    --pill:#2f87c9;
    --pill-dark:#1f6fb4;
    --storm:#2b4a98;
    --black:#000;
    --white:#fff;
    --ink:#1c3a8a;
    --badge:#e3ecf6;
  }
  *{margin:0;padding:0;box-sizing:border-box}
  html,body{width:1200px;height:435px;overflow:hidden;background:var(--page)}
  .billboard{position:absolute;left:0;top:42px;width:1200px;height:350px;overflow:hidden;
    background:linear-gradient(90deg,var(--sky) 0%,var(--navy) 14%,var(--deep) 55%,var(--storm) 100%)}
  .storm-scene{position:absolute;left:680px;top:0;width:520px;height:287px;
    background:linear-gradient(180deg,rgba(60,100,190,.35) 0%,rgba(40,80,170,.55) 55%,rgba(90,130,210,.6) 80%,rgba(30,60,140,.7) 100%)}
  .brand-mark{position:absolute;left:38px;top:38px;width:152px;height:152px;border-radius:50%;
    background:var(--white);display:flex;align-items:center;justify-content:center}
  .brand-mark span{font-family:"Montserrat",sans-serif;font-weight:700;font-size:20px;color:var(--ink);letter-spacing:1px}
  .identity{position:absolute;left:262px;top:36px;width:446px;color:var(--white);text-align:center}
  .identity .name{font-family:"Cinzel",serif;font-weight:600;font-size:44px;line-height:1;white-space:nowrap}
  .identity .sub{display:flex;align-items:center;justify-content:center;gap:16px;margin-top:6px}
  .identity .sub i{display:block;height:3px;width:86px;background:var(--white);border-radius:2px}
  .identity .sub span{font-family:"Cinzel",serif;font-weight:600;font-size:28px;letter-spacing:6px;line-height:1}
  .identity .tagline{font-family:"Open Sans",sans-serif;font-style:italic;font-weight:700;font-size:25px;margin-top:16px;white-space:nowrap}
  .identity .motto{font-family:"Cinzel",serif;font-weight:500;font-size:28px;margin-top:12px;white-space:nowrap}
  .headline{position:absolute;left:736px;top:42px;width:480px;height:164px;border:3px solid var(--white);border-right:none;
    border-radius:82px 0 0 82px;background:linear-gradient(180deg,var(--pill) 0%,var(--pill-dark) 100%);
    display:flex;align-items:center;justify-content:center;padding-right:20px}
  .headline p{font-family:"Cinzel",serif;font-weight:700;font-size:40px;line-height:42px;color:var(--white);text-align:center;
    text-shadow:2px 3px 4px rgba(0,0,0,.5)}
  .band{position:absolute;left:0;top:245px;width:718px;height:42px;background:var(--black);
    clip-path:polygon(0 0,703px 0,718px 42px,0 42px);display:flex;align-items:center;padding-left:31px}
  .band span{font-family:"Montserrat",sans-serif;font-weight:700;font-size:14.4px;color:var(--white);letter-spacing:.4px;white-space:nowrap}
  .reviews-title{position:absolute;left:760px;top:250px;width:430px;text-align:center;
    font-family:"Montserrat",sans-serif;font-weight:600;font-size:16px;color:var(--white)}
  .footer{position:absolute;left:0;top:287px;width:1200px;height:63px;background:var(--white)}
  .contact{position:absolute;display:flex;align-items:center;color:var(--ink);font-family:"Montserrat",sans-serif;white-space:nowrap}
  .contact.phone{left:30px;top:12px;font-size:27px;font-weight:600;gap:11px}
  .contact.phone b{font-weight:700}
  .contact.email{left:384px;top:20px;font-size:15.5px;font-weight:600;gap:8px}
  .awards{position:absolute;left:798px;top:9px;display:flex;align-items:center;gap:16px}
  .awards .rating-badge{width:92px;height:44px;border-radius:4px;background:var(--badge)}
  .awards .accredit-badge{width:38px;height:42px;border-radius:4px;background:var(--ink)}
  .awards .listing{font-family:"Montserrat",sans-serif;font-weight:700;font-size:20px;color:var(--ink)}
</style>
</head>
<body>
  <section class="billboard">
    <div class="storm-scene" role="img" aria-label="Stormy hurricane coastline with palm trees and crashing waves"></div>

    <div class="brand-mark"><span>CEDARLINE</span></div>

    <div class="identity">
      <div class="name">The Cedarline</div>
      <div class="sub"><i></i><span>Claim Help</span><i></i></div>
      <div class="tagline">EXPERT &amp; LOCAL Public Adjusters</div>
      <div class="motto">"For the Policyholder!!"</div>
    </div>

    <div class="headline"><p>Don't let<br>the Hurricane<br>Ruin Your Life!!</p></div>

    <div class="band"><span>20+ YEARS OF EXPERIENCE, RECOVERING MILLIONS FOR OUR VIP CLIENTS</span></div>
    <div class="reviews-title">5 Star Reviews, Ratings &amp; Awards</div>

    <div class="footer">
      <div class="contact phone">
        <svg width="27" height="27" viewBox="0 0 28 28" aria-hidden="true">
          <circle cx="14" cy="14" r="14" fill="#1c3a8a"/>
          <path d="M9.5 7.5l2.6-.4 1.4 3.3-1.6 1.2c.8 1.8 2 3 3.8 3.8l1.2-1.6 3.3 1.4-.4 2.6c-5.6.4-10.7-4.7-10.3-10.3z" fill="#fff"/>
        </svg>
        <span>Call us <b>850-555-0142</b></span>
      </div>
      <div class="contact email">
        <svg width="17" height="17" viewBox="0 0 18 18" aria-hidden="true">
          <circle cx="9" cy="9" r="9" fill="#1c3a8a"/>
          <rect x="4.5" y="6" width="9" height="6.5" rx="1" fill="#fff"/>
          <path d="M4.8 6.4L9 9.6l4.2-3.2" stroke="#1c3a8a" stroke-width="1" fill="none"/>
        </svg>
        <span>marcus@CedarlineClaimHelp.com</span>
      </div>
      <div class="awards">
        <div class="rating-badge"></div>
        <div class="accredit-badge"></div>
        <span class="listing">Zorvex</span>
        <span class="listing">PORCHLINK</span>
      </div>
    </div>
  </section>
</body>
</html>
```